Marketing Business Card Design

I am, launching a marketing business where I will contract to market hospitality. I want something funky and fun to go with the name Maple Kettle

Industry/Entity Type

Marketing

Contact Information for Business Card

Nora Feltham-Quince
Maple Kettle
Mobile: +61 2 407 652390
Email: nora@maplekettle.com.au

Requirements
Must have
• Fun and modern
Should not have
• Not conservative

```html
<!DOCTYPE html>
<html lang="en">
<head>
<meta charset="utf-8">
<title>Maple Kettle — Business Card</title>
<link rel="stylesheet" href="https://fonts.googleapis.com/css2?family=Quicksand:wght@300;400;500;700&display=swap">
<style>
  :root {
    --brand-red: #c4161c;
    --card-white: #ffffff;
    --text-grey: #5a5a5a;
    --font-main: "Quicksand", sans-serif;
  }
  * { margin: 0; padding: 0; box-sizing: border-box; }
  html, body {
    width: 721px;
    height: 1200px;
    overflow: hidden;
    background: var(--brand-red);
  }
  .business-card {
    position: relative;
    width: 721px;
    height: 1200px;
    background: var(--brand-red);
    font-family: var(--font-main);
  }
  .card-panel {
    position: absolute;
    left: 60px;
    top: 61px;
    width: 598px;
    height: 1074px;
    background: var(--card-white);
    border-radius: 16px;
  }
  .brand-name {
    position: absolute;
    left: 0;
    width: 721px;
    top: 276px;
    text-align: center;
    font-size: 70px;
    font-weight: 700;
    line-height: 80px;
    color: var(--brand-red);
    letter-spacing: 1px;
  }
  .person-name {
    position: absolute;
    left: 0;
    width: 721px;
    top: 622px;
    text-align: center;
    font-size: 41px;
    font-weight: 500;
    color: var(--brand-red);
    line-height: 50px;
  }
  .contact-list {
    position: absolute;
    left: 143px;
    top: 787px;
    width: 490px;
    list-style: none;
  }
  .contact-item {
    display: flex;
    align-items: center;
    height: 70px;
    margin-bottom: 36px;
  }
  .contact-badge {
    width: 70px;
    height: 70px;
    border-radius: 50%;
    background: var(--brand-red);
    color: var(--card-white);
    display: flex;
    align-items: center;
    justify-content: center;
    font-weight: 700;
    font-style: italic;
    font-size: 30px;
    flex-shrink: 0;
  }
  .contact-badge--small { font-size: 24px; letter-spacing: -1px; }
  .contact-value {
    margin-left: 28px;
    color: var(--text-grey);
    font-weight: 300;
    font-size: 37px;
    letter-spacing: 1px;
    white-space: nowrap;
  }
  .contact-value--email { font-size: 29px; letter-spacing: 0; }
</style>
</head>
<body>
  <main class="business-card">
    <div class="card-panel"></div>
    <div class="brand-name">Maple Kettle</div>
    <h1 class="person-name">Nora Feltham-Quince</h1>
    <ul class="contact-list">
      <li class="contact-item">
        <span class="contact-badge">M</span>
        <span class="contact-value">+61 2 407 652390</span>
      </li>
      <li class="contact-item">
        <span class="contact-badge">E</span>
        <span class="contact-value contact-value--email">nora@maplekettle.com.au</span>
      </li>
      <li class="contact-item">
        <span class="contact-badge contact-badge--small">ABN</span>
        <span class="contact-value">51836074219</span>
      </li>
    </ul>
  </main>
</body>
</html>
```